Business Consultancy Wordpress Design

Small business analysis consultancy.

Looking for a bold, clean design for Wordpress. Final site will only be a few pages, some contact information, services provided and a little background information. Potentially a blog.

Colours to be as per logo, with either black or white as the main colour.

Link is www.halvicadvisory.com

More details to be included in the best few days

Name - Halvic Consulting
Provides - Project Consultancy
Updates

Project Deadline Extended
Reason: I am going to be on holiday with little access to the web over 28/02 - 05/03 and am therefore extending the deadline

Target Market(s)

Business professionals

Industry/Entity Type

Business

Colors

Designer to choose colors to be used in the design.

Requirements
Must have
• Must contain the logo in the header
Footer must fit a 3 column layout in wordpress

Business style, royalty free stock images
Nice to have
• Would like the 1 or 2 column wordpress style layout
Should not have
• must not be blog or magazine style layout or look and feel

```html
<!DOCTYPE html>
<html lang="en">
<head>
<meta charset="utf-8">
<title>Halvic Consulting</title>
<link href="https://fonts.googleapis.com/css2?family=Lato:wght@300;400;700&display=swap" rel="stylesheet">
<style>
:root{
  --blue:#0f9bd9;
  --blue-deep:#0a6fae;
  --green:#6ab42d;
  --ink:#333c44;
  --muted:#8c979f;
  --soft-bg:#eef3f7;
  --footer:#2e3840;
  --footer-base:#252d33;
  --footer-text:#a5b0b8;
  --white:#fff;
}
*{box-sizing:border-box;margin:0;padding:0}
html,body{width:1024px;height:1200px;overflow:hidden}
body{font-family:'Lato',sans-serif;background:var(--white);position:relative;color:var(--ink)}
.abs{position:absolute}
.topbar{left:0;top:0;width:1024px;height:31px;border-bottom:1px solid #e6e9ec;font-size:9px;color:#a5aeb5}
.topbar .contact-strip{position:absolute;right:122px;top:9px;display:flex;align-items:center;gap:20px;white-space:nowrap}
.topbar .item{display:flex;align-items:center;gap:7px}
.header{left:0;top:31px;width:1024px;height:73px}
.brand{left:126px;top:14px;display:flex;align-items:center;gap:12px}
.brand-mark{width:44px;height:44px;border-radius:50%;background:var(--blue)}
.brand-name{font-size:26px;font-weight:400;color:#6d7479;letter-spacing:.2px;text-transform:uppercase}
.nav{right:123px;top:30px;display:flex;gap:37px;font-size:12px;color:#5b646b}
.nav .active{color:var(--blue)}
.hero{left:0;top:104px;width:1024px;height:384px;background:linear-gradient(100deg,#5d6b77 0%,#8d9aa5 35%,#2f3e58 55%,#a9b4bd 80%,#d5dbdf 100%)}
.hero-panel{left:0;top:106px;width:540px;height:146px;background:rgba(8,110,180,.82);color:var(--white);padding:38px 0 0 152px}
.hero-panel h1{font-weight:300;font-size:25px;margin-bottom:14px}
.hero-panel p{font-size:10.5px;line-height:16px;width:360px}
.dots{left:846px;top:359px;display:flex;gap:8px}
.dots span{width:8px;height:8px;border-radius:50%;background:var(--white)}
.dots .on{background:var(--blue);box-shadow:0 0 0 2px var(--white)}
.welcome{left:0;top:488px;width:1024px;height:400px;background:var(--soft-bg)}
.welcome h2{position:absolute;top:32px;width:100%;text-align:center;font-weight:300;font-size:25px;color:var(--ink)}
.welcome .lead{position:absolute;top:76px;left:332px;width:360px;text-align:center;font-size:10.5px;line-height:16px;color:var(--muted)}
.card{top:133px;width:246px}
.card .photo{height:144px}
.card h3{margin-top:14px;font-weight:400;font-size:12.5px;color:var(--ink)}
.card p{margin-top:7px;font-size:10.5px;line-height:16px;color:var(--muted)}
.card.current .photo{border:1px solid var(--blue);border-bottom:4px solid #5bb6e6}
.card.current h3{color:var(--blue)}
.plus{left:103px;top:53px;width:38px;height:38px;border-radius:50%;background:rgba(15,155,217,.85);color:var(--white);font-size:24px;font-weight:300;text-align:center;line-height:36px}
.footer{left:0;top:888px;width:1024px;height:274px;background:var(--footer);color:var(--footer-text);font-size:10.5px;line-height:16px}
.footer h4{font-size:12.5px;font-weight:700;color:#e7ecef;margin-bottom:16px}
.f-brand{display:flex;align-items:center;gap:7px;margin-bottom:14px}
.f-brand .dot{width:20px;height:20px;border-radius:50%;background:var(--blue)}
.f-brand span{font-size:12.5px;color:#8f9aa2;text-transform:uppercase}
.more{font-size:9px;text-decoration:underline;color:#9aa5ad;letter-spacing:.3px}
.post{display:flex;gap:11px;margin-bottom:11px}
.post .thumb{width:44px;height:44px;flex:none;background:linear-gradient(135deg,#c9d3da,#5d6a74)}
.post .date{font-size:9px;color:#7c878f}
.social{display:flex;gap:13px;margin-bottom:34px}
.social span{width:26px;height:26px;border-radius:50%;background:#56616a}
.subscribe{display:flex;margin-top:14px;height:29px}
.subscribe .field{width:130px;background:#1f272d;color:#c7cfd5;padding:8px 0 0 10px}
.subscribe .btn{width:70px;background:var(--blue);color:var(--white);text-align:center;padding-top:8px}
.contact-row{display:flex;gap:12px;margin-bottom:8px}
.contact-row svg{flex:none;margin-top:2px}
.map{width:155px;height:63px;margin-top:26px;border-radius:2px;background:linear-gradient(135deg,#e8e4d8,#d8d6cc 50%,#f0e6a0)}
.base{left:0;top:1162px;width:1024px;height:38px;background:var(--footer-base);font-size:10.5px;color:#8f9aa2}
.base .copy{position:absolute;left:121px;top:12px}
.base .links{position:absolute;right:122px;top:12px;display:flex;gap:37px}
.base .links .active{color:#e7ecef}
</style>
</head>
<body>
<div class="abs topbar">
  <div class="contact-strip">
    <div class="item">
      <svg width="24" height="11" viewBox="0 0 24 11"><path d="M0 2h5M2 5h3M0 8h5" stroke="#8ccbe8" stroke-width="1"/><rect x="8" y="1" width="15" height="9" fill="none" stroke="#8ccbe8"/><path d="M8 1l7.5 5L23 1" fill="none" stroke="#8ccbe8"/></svg>
      <span>info@halvicadvisory.com</span>
    </div>
    <div class="item">
      <svg width="14" height="13" viewBox="0 0 14 13"><path d="M3 1l2 3-1 1.5c1 2 2.5 3.5 4 4l1.5-1 3 2-1.5 2C6 12 1 7 1 2z" fill="#8ccbe8"/></svg>
      <span>+1 555.010.2040</span>
    </div>
  </div>
</div>

<header class="abs header">
  <div class="abs brand"><span class="brand-mark"></span><span class="brand-name">Halvic Consulting</span></div>
  <nav class="abs nav"><span class="active">Home</span><span>Services</span><span>Blog</span><span>About</span><span>Contact</span></nav>
</header>

<section class="abs hero" role="img" aria-label="Photo of a businessman in glasses talking on a phone on a city street">
  <div class="abs hero-panel">
    <h1>We Move Businesses Forward</h1>
    <p>Maecenas bibendum lacus gravida placerat consequat. Vivamus quis hendrerit mauris. Vestibulum laoreet felis sed consectetur sollicitudin.</p>
  </div>
  <div class="abs dots"><span></span><span class="on"></span><span></span><span></span></div>
</section>

<section class="abs welcome">
  <h2>Welcome to Halvic Consulting</h2>
  <p class="lead">Maecenas bibendum lacus gravida placerat consequat. Vivamus quis hendrerit mauris. Vestibulum laoreet felis sed consectetur sollicitudin.</p>

  <article class="abs card" style="left:120px">
    <div class="photo" role="img" aria-label="Photo of a team working together at a laptop" style="background:linear-gradient(135deg,#d9dde0,#6b737a 60%,#2c3135)"></div>
    <h3>Our Mission</h3>
    <p>Lorem ipsum dolor sit amet, consectetur adipisicing elit, sed do eiusmod tempor incididunt ut labore et dolore magna aliqua.</p>
  </article>

  <article class="abs card current" style="left:390px">
    <div class="photo" style="position:relative;background:linear-gradient(135deg,#eef1f3,#a7b2ba 50%,#5f6b74)" role="img" aria-label="Photo of colleagues reviewing work on a laptop">
      <div class="abs plus">+</div>
    </div>
    <svg class="abs" style="left:227px;top:147px" width="19" height="20" viewBox="0 0 19 20"><path d="M0 0h19v20z" fill="#5bb6e6"/></svg>
    <h3>Our Values</h3>
    <p>Lorem ipsum dolor sit amet, consectetur adipisicing elit, sed do eiusmod tempor incididunt ut labore et dolore magna aliqua.</p>
  </article>

  <article class="abs card" style="left:657px">
    <div class="photo" role="img" aria-label="Photo of three professionals looking at a tablet" style="background:linear-gradient(135deg,#f1f2f3,#a9a39c 50%,#3b4148)"></div>
    <h3>Our Solution</h3>
    <p>Lorem ipsum dolor sit amet, consectetur adipisicing elit, sed do eiusmod tempor incididunt ut labore et dolore magna aliqua.</p>
  </article>
</section>

<footer class="abs footer">
  <div class="abs" style="left:121px;top:40px;width:170px">
    <div class="f-brand"><span class="dot"></span><span>Halvic Consulting</span></div>
    <p style="margin-bottom:8px">Fusce gravida tortor felis, ac dictum risus sagittis id.</p>
    <p style="margin-bottom:16px">Donec volutpat, mi vel egestas eleif-end, dolor arcu iaculis nunc. Fusce gravida tortor felis, ac dictum risus sagittis id. Morbi posuere justo eleif-end libero ultricies ultrices.</p>
    <span class="more">LEAR MORE</span>
  </div>

  <div class="abs" style="left:322px;top:43px;width:180px">
    <h4>Recent Post</h4>
    <div class="post"><div class="thumb" role="img" aria-label="Post thumbnail photo"></div><div>Fusce gravida tortor felis, ac dictum risus sagittis<div class="date">October 15, 2013</div></div></div>
    <div class="post"><div class="thumb" role="img" aria-label="Post thumbnail photo"></div><div style="color:#e7ecef">Fusce gravida tortor felis, ac dictum risus sagittis<div class="date">October 15, 2013</div></div></div>
    <div class="post"><div class="thumb" role="img" aria-label="Post thumbnail photo"></div><div>Fusce gravida tortor felis, ac dictum risus sagittis<div class="date">October 15, 2013</div></div></div>
  </div>

  <div class="abs" style="left:526px;top:43px;width:200px">
    <h4>Get Social</h4>
    <div class="social"><span></span><span></span><span></span><span></span></div>
    <h4 style="margin-bottom:14px">Newsletter</h4>
    <p>Ipsum dolor sit amet, teft consecte tur adipiscing elit ut eunt.</p>
    <div class="subscribe"><div class="field">Email Address</div><div class="btn">Subscribe</div></div>
  </div>

  <div class="abs" style="left:743px;top:43px;width:170px">
    <h4>Contact Details</h4>
    <div class="contact-row"><svg width="13" height="12" viewBox="0 0 14 13"><path d="M3 1l2 3-1 1.5c1 2 2.5 3.5 4 4l1.5-1 3 2-1.5 2C6 12 1 7 1 2z" fill="#7c878f"/></svg>+1-555-010-2040</div>
    <div class="contact-row"><svg width="13" height="12" viewBox="0 0 13 12"><rect x="1" y="2" width="11" height="8" fill="none" stroke="#7c878f" stroke-width="1.3"/><path d="M1 2l5.5 4L12 2" fill="none" stroke="#7c878f" stroke-width="1.3"/></svg>hello@halvicadvisory.com</div>
    <div class="contact-row"><svg width="13" height="15" viewBox="0 0 13 15"><path d="M6.5 1a4.5 4.5 0 0 1 4.5 4.5C11 9 6.5 14 6.5 14S2 9 2 5.5A4.5 4.5 0 0 1 6.5 1z" fill="#7c878f"/><circle cx="6.5" cy="5.5" r="1.7" fill="#2e3840"/></svg>Your Address, Your Country<br>Your Zip Code</div>
    <div class="map" role="img" aria-label="Small street map showing the office location"></div>
  </div>
</footer>

<div class="abs base">
  <span class="copy">Copyright © 2014 - Halvic Consulting. All Rights reserved</span>
  <nav class="links"><span class="active">Home</span><span>Services</span><span>Blog</span><span>About</span><span>Contact</span></nav>
</div>
</body>
</html>
```